In house, web site post, social media post, and email blast specials/promo flyer

We are looking to update our monthly specials flyer to be sent out via Constant Contacts as well as printed and handed out in office and social media and posted to our website. Please see attachments below for a sample of a previous flyer. We want it to look clean and not too busy. It should be professional looking as this is going to a higher end client that is paying cash for our services

Target Market(s)

Women and Men 35-55

Contact Information for Business Card

I am tired of our current business card and want a fresh updated look. We want something simple, clean, and modern looking.

Font styles to use
Sans Serif
Script

Colors
3377b5
34a7d8
85cae6
85abd2
cedeed
ecf7fb
eaf1f7

Requirements
Must have
• Clean lines, Sexy, appealing to the medical spa beauty industry. Our clients come to us to look and feel good.
• Content of actual specials:
• FIGHT FINE LINES AND WRINKLES-Purchase a minimum of 30 units of Velmox and receive a complimentary Glycolic Acid Peel ($150 VALUE)
• THE SWEAT STOPS HERE-Permanently stop underarm sweat with TessaCool treatments, starting at $1,950
• BRIGHTEN & TONE-IPL $ Laser Lumora package $3,500
• REDUCE FACE & LEG VEINS- 15% off packages
• FLORENZA: CHEEKS & NL FOLDS-SECOND SYRINGE 25% OFF, THIRD SYRINGE $50 OFF
• BODY SCULPTING FOR ABDOMEN AND THIGHS-Blast unwanted fat with a trio of treatments! $4,799
Nice to have
• Here are some sample flyers of what we would like ours to look like
• https://www.kelbrooskinspa.example/specials/
• https://marvellisaesthetics.example/november-specials-2017/

```html
<!DOCTYPE html>
<html lang="en">
<head>
<meta charset="utf-8">
<title>Solenne Aesthetic &amp; Anti-Aging Center — Business Card</title>
<link rel="stylesheet" href="https://fonts.googleapis.com/css2?family=Montserrat:wght@400;700&family=Questrial&display=swap">
<style>
  :root {
    --page-bg: #eef1f4;
    --brand-blue: #3377b5;
    --brand-blue-light: #85abd2;
    --brand-gold: #a9a032;
    --card-white: #ffffff;
    --card-mist: #ecf7fb;
    --ink: #2a2f36;
    --logo-ink: #34505c;
    --photo-green: #4f7d4a;
    --photo-skin: #d9a98c;
  }
  html, body {
    margin: 0;
    padding: 0;
    width: 1200px;
    height: 1200px;
    overflow: hidden;
    background: var(--page-bg);
  }
  .sheet {
    width: 1200px;
    height: 1200px;
    display: flex;
    flex-direction: column;
    align-items: center;
    justify-content: center;
    gap: 70px;
  }
  .card {
    width: 840px;
    height: 480px;
    display: block;
    box-shadow: 0 10px 28px rgba(0,0,0,0.18);
  }
  .card-title {
    font-family: "Montserrat", sans-serif;
    font-weight: 700;
    font-size: 34px;
    fill: var(--card-white);
    letter-spacing: 0.5px;
  }
  .card-subtitle {
    font-family: "Montserrat", sans-serif;
    font-weight: 400;
    font-size: 30px;
    fill: var(--brand-gold);
    letter-spacing: 0.5px;
  }
  .brand-name {
    font-family: "Questrial", sans-serif;
    font-size: 50px;
    fill: var(--logo-ink);
  }
  .contact-line {
    font-family: "Questrial", sans-serif;
    font-size: 17px;
    fill: var(--ink);
  }
  .contact-icon { fill: var(--brand-gold); }
  .contact-icon-stroke { fill: none; stroke: var(--brand-gold); stroke-width: 1.6; }
</style>
</head>
<body>
<main class="sheet">

  <!-- Front of card -->
  <svg class="card card-front" viewBox="0 0 840 480" xmlns="http://www.w3.org/2000/svg">
    <defs>
      <linearGradient id="front-photo-tone" x1="0" y1="0" x2="1" y2="1">
        <stop offset="0" stop-color="var(--photo-green)"/>
        <stop offset="0.45" stop-color="var(--photo-skin)"/>
        <stop offset="1" stop-color="#8a5a3c"/>
      </linearGradient>
      <linearGradient id="front-blue" x1="0" y1="0" x2="1" y2="0">
        <stop offset="0" stop-color="var(--brand-blue)"/>
        <stop offset="1" stop-color="var(--brand-blue-light)"/>
      </linearGradient>
      <linearGradient id="front-white" x1="0" y1="0" x2="0" y2="1">
        <stop offset="0" stop-color="var(--card-white)"/>
        <stop offset="1" stop-color="var(--card-mist)"/>
      </linearGradient>
    </defs>
    <rect class="card-photo" x="0" y="0" width="600" height="480" fill="url(#front-photo-tone)" role="img" aria-label="Photo of a relaxed spa client resting with a white flower in her hair"/>
    <path class="card-band-blue" d="M0 0 L605 0 C560 70 520 140 495 210 C320 185 160 185 0 215 Z" fill="url(#front-blue)"/>
    <path class="card-swoosh-gold" d="M560 150 C500 270 460 380 372 480 L420 480 C470 360 520 250 560 150 Z" fill="var(--brand-gold)"/>
    <path class="card-panel-white" d="M600 0 C520 130 480 330 420 480 L840 480 L840 0 Z" fill="url(#front-white)"/>
    <text class="card-title" x="36" y="92">SOLENNE AESTHETIC &amp;</text>
    <text class="card-subtitle" x="36" y="134">ANTI-AGING CENTER</text>
    <rect class="brand-mark" x="530" y="222" width="12" height="12" fill="var(--brand-gold)"/>
    <text class="brand-name" x="552" y="252" textLength="250" lengthAdjust="spacingAndGlyphs">SOLENNE</text>
  </svg>

  <!-- Back of card -->
  <svg class="card card-back" viewBox="0 0 840 480" xmlns="http://www.w3.org/2000/svg">
    <defs>
      <linearGradient id="back-photo-tone" x1="0" y1="0" x2="1" y2="1">
        <stop offset="0" stop-color="var(--photo-green)"/>
        <stop offset="0.5" stop-color="var(--photo-skin)"/>
        <stop offset="1" stop-color="#b88a66"/>
      </linearGradient>
      <linearGradient id="back-blue" x1="0" y1="0" x2="1" y2="0">
        <stop offset="0" stop-color="var(--brand-blue)"/>
        <stop offset="1" stop-color="var(--brand-blue-light)"/>
      </linearGradient>
      <linearGradient id="back-white" x1="0" y1="0" x2="0" y2="1">
        <stop offset="0" stop-color="var(--card-white)"/>
        <stop offset="1" stop-color="var(--card-mist)"/>
      </linearGradient>
    </defs>
    <rect class="card-photo" x="360" y="0" width="480" height="320" fill="url(#back-photo-tone)" role="img" aria-label="Photo of a spa client relaxing with eyes closed and a white flower in her hair"/>
    <path class="card-band-blue" d="M0 0 L520 0 C545 110 525 215 470 292 C300 300 150 330 0 382 Z" fill="url(#back-blue)"/>
    <path class="card-swoosh-gold" d="M0 366 C200 300 450 276 840 282 L840 312 C450 302 200 322 0 392 Z" fill="var(--brand-gold)"/>
    <path class="card-panel-white" d="M0 392 C200 322 450 306 840 312 L840 480 L0 480 Z" fill="url(#back-white)"/>
    <text class="card-title" x="36" y="200">SOLENNE AESTHETIC &amp;</text>
    <text class="card-subtitle" x="36" y="240">ANTI-AGING CENTER</text>

    <g class="contact-list">
      <g class="contact-icon" transform="translate(176 364)">
        <rect x="0" y="4" width="14" height="9" rx="1"/>
        <rect x="3" y="0" width="8" height="5" fill="var(--card-white)" stroke="var(--brand-gold)" stroke-width="1.2"/>
      </g>
      <text class="contact-line" x="198" y="377">fax (555) 014-2281</text>
      <g transform="translate(183 389)">
        <circle class="contact-icon-stroke" cx="0" cy="0" r="7"/>
        <ellipse class="contact-icon-stroke" cx="0" cy="0" rx="3" ry="7"/>
        <line class="contact-icon-stroke" x1="-7" y1="0" x2="7" y2="0"/>
      </g>
      <text class="contact-line" x="198" y="395">www.solenneclinic.example</text>
      <g transform="translate(176 401)">
        <rect class="contact-icon" x="0" y="0" width="14" height="10" rx="1"/>
        <path d="M0 0 L7 6 L14 0" fill="none" stroke="var(--card-white)" stroke-width="1.2"/>
      </g>
      <text class="contact-line" x="198" y="413">info@solenneclinic.example</text>
      <path class="contact-icon" transform="translate(176 419)" d="M2 0 L5 0 L6 4 L4 5.5 C5 8 6.5 9.5 9 10.5 L10.5 8.5 L14 9.5 L14 12.5 C14 13.3 13.3 14 12.5 14 C5.5 13.5 0.5 8.5 0 1.5 C0 0.7 0.9 0 2 0 Z"/>
      <text class="contact-line" x="198" y="431">(555) 014-3390, (555) 014-7712</text>
      <path class="contact-icon" transform="translate(177 436)" d="M6 0 C9.3 0 12 2.6 12 5.8 C12 10 6 16 6 16 C6 16 0 10 0 5.8 C0 2.6 2.7 0 6 0 Z M6 3.5 A2.3 2.3 0 1 0 6 8.1 A2.3 2.3 0 1 0 6 3.5 Z" fill-rule="evenodd"/>
      <text class="contact-line" x="198" y="449">2210 NW Alder Row, Suite 2 Portland,</text>
      <text class="contact-line" x="198" y="468">OR 97000</text>
    </g>
  </svg>

</main>
</body>
</html>
```